Brightvale Fluid Systems Corp Business Cards

Business cards to match the logo.

Company is a start up water technology company that has developed a patented system using centrifugal force to separate waste from municipal waste water to produce crystal clear clean water. Product sell starting at 2 million to governments both in the US and international.

Business cards should have a professional look with the target generally engineers.

Target Market(s)

Engineers, Government officials and investors

Industry/Entity Type

Water Treatment

Contact Information for Business Card

Business cards design will be used for 6 to 8 people with job titles. Can use the quote "If there is magic in the planet, it is contained in water." but not required to use quote. Should follow theme of Logo

Font styles to use
Other font styles liked:
• match logo font

Requirements
Nice to have
• Colors to match Logo. Business cards to match style of flow of Logo.
• Emphasis on clean look not a busy look. Clean flowing water.
Should not have
• Pictures of industrial equipment or wastewater

```html
<!DOCTYPE html>
<html lang="en">
<head>
<meta charset="utf-8">
<title>Brightvale Fluid Systems – Business Cards</title>
<link href="https://fonts.googleapis.com/css2?family=Lato:wght@400;700&display=swap" rel="stylesheet">
<style>
  :root {
    --navy: #22527a;
    --sky: #3ba4dc;
    --ink: #1d2a36;
    --paper: #ffffff;
    --backdrop: #d9dcdf;
    --rule: #4a6f92;
  }
  * { box-sizing: border-box; margin: 0; padding: 0; }
  html, body {
    width: 1200px; height: 1059px; overflow: hidden;
    background: var(--backdrop);
    font-family: "Lato", Arial, sans-serif;
  }
  .sheet {
    position: relative; width: 1200px; height: 1059px;
  }
  .card {
    position: absolute; left: 250px; width: 700px; height: 400px;
    box-shadow: 0 6px 18px rgba(0,0,0,0.18);
    overflow: hidden;
  }
  /* Front */
  .card--front { top: 90px; background: var(--navy); color: var(--paper); }
  .front__brand {
    position: absolute; left: 0; right: 0; top: 150px;
    text-align: center; font-weight: 700; font-size: 42px; letter-spacing: 1px;
  }
  .front__tagline {
    position: absolute; left: 0; right: 0; bottom: 40px;
    text-align: center; font-size: 15px; letter-spacing: 0.5px; text-transform: uppercase;
  }
  /* Back */
  .card--back { top: 570px; background: var(--paper); color: var(--ink); }
  .back__wave { position: absolute; inset: 0; }
  .back__brand {
    position: absolute; left: 40px; top: 140px; width: 300px;
    text-align: center; font-weight: 700; font-size: 30px; line-height: 1.15; color: var(--navy);
  }
  .back__divider {
    position: absolute; left: 375px; top: 55px; width: 1.5px; height: 150px; background: var(--rule);
  }
  .contact { position: absolute; left: 405px; top: 40px; font-size: 16px; line-height: 1.3; }
  .contact__name { color: var(--navy); font-weight: 700; font-size: 22px; }
  .contact__title { font-size: 14px; margin-bottom: 12px; }
  .contact__address { margin-bottom: 10px; }
  .contact__line { display: flex; align-items: center; gap: 8px; }
  .contact__line svg { width: 13px; height: 13px; fill: var(--navy); flex: none; }
  .back__url {
    position: absolute; right: 60px; bottom: 38px; color: var(--paper); font-size: 18px; letter-spacing: 0.5px;
  }
</style>
</head>
<body>
<main class="sheet">
  <section class="card card--front" aria-label="Card front">
    <div class="front__brand">BRIGHTVALE FLUID SYSTEMS</div>
    <p class="front__tagline">If there is magic in the planet, it is contained in water.</p>
  </section>

  <section class="card card--back" aria-label="Card back">
    <svg class="back__wave" viewBox="0 0 700 400" preserveAspectRatio="none" aria-hidden="true">
      <path d="M0,385 C250,360 480,262 700,218 L700,238 C480,284 250,372 0,392 Z" fill="var(--sky)"/>
      <path d="M0,400 L0,396 C250,378 480,296 700,248 L700,400 Z" fill="var(--navy)"/>
    </svg>
    <div class="back__brand">BRIGHTVALE FLUID SYSTEMS</div>
    <div class="back__divider"></div>
    <div class="contact">
      <div class="contact__name">Daniel Hartley</div>
      <div class="contact__title">Manager</div>
      <div class="contact__address">418 Cedar Brook Lane<br>Houston, TX 77041</div>
      <div class="contact__line">
        <svg viewBox="0 0 24 24"><path d="M6.6 10.8a15 15 0 0 0 6.6 6.6l2.2-2.2a1 1 0 0 1 1-.25 11.4 11.4 0 0 0 3.6.57 1 1 0 0 1 1 1V20a1 1 0 0 1-1 1A17 17 0 0 1 3 4a1 1 0 0 1 1-1h3.5a1 1 0 0 1 1 1c0 1.25.2 2.45.57 3.6a1 1 0 0 1-.25 1z"/></svg>
        <span>512 555 0142</span>
      </div>
      <div class="contact__line">
        <svg viewBox="0 0 24 24"><path d="M6 2h9l3 3v5H6zM3 11h18v8h-3v3H6v-3H3zm5 5v4h8v-4z"/></svg>
        <span>512 555 0143</span>
      </div>
      <div class="contact__line">
        <svg viewBox="0 0 24 24"><path d="M2 5h20v14H2zm2 2v.5l8 5 8-5V7l-8 5z"/></svg>
        <span>info@brightvalefluid.com</span>
      </div>
    </div>
    <div class="back__url">www.brightvalefluid.com</div>
  </section>
</main>
</body>
</html>
```